Marktplatz Flohmarkt Kleinanzeigen Marktplatz
Zielgruppe
Wir sind ein Marktplatz rund um Hochzeit. D.h. bei uns können kostenlos alle Sachen (Brautkleid, Brautschuhe, Braut Accessories, Hochzeits Dekoration) zum verkauf eingestellt werden. Wie tauscho inserate, nur eben spezialisiert auf Hochzeit
Aufgabenstellung
Wir benötigen für unseren PHP Marktplatz ein Design, welches sehr Modern und ansprechend ist. Wir möchten kein Klassisches Hochzeitsportal mit den Üblichen Rosa, Beigen Farben sein, sondern möchten vor allem die Junge Zielgruppe ansprechen.
Das Design soll ein Mix aus tauscho-inserate und Stoffwandel sein, wobei uns wichtiger wäre das man sich bewusst am design von Stoffwandel orientiert.
Was uns besonders an Stoffwandel gefällt ist im Header die farbliche Leiste wo Logo und Kategorien integriert sind. Schicht und einfach, ohne schnickschnack.
ebenso wie bei Stoffwandel wird bei uns auf der Startseite folgendes integriert:
-Werbung (Banner)
-Plaudernetz
-Forum
Aktuelle menüs auf der Startseite:
-Home
-Marktplatz
-Gesuche (wobei gesuche kann im Layout integriert werden)
-Dienstleister (Händler und Dienstleister)
-Gruppen (das kann en einer anderen Stelle integriert werden)
-Forum (noch nicht integriert, aber beachten beim Layout, da es eingebaut wird)
-Veranstaltungen / Events
-Über Uns
(alles was aktuell im Screenshot zu sehen ist, wird aus der Leiste entfernt und im Footer eingebaut)
Anhang:
-Logo
-Screenshot unseres Aktuellen marktplatzes (noch nicht Online)
-Screenshot von StoffWandel
Design:
-Startseite
-Artikelseite (wenn der Private Kunde eine anzeige einstellt)
-Ansprechende Anmeldeseite inkl. Darstellung unserer Pakete für Privat / Händler / Dienstleister

```html
<!DOCTYPE html>
<html lang="de">
<head>
<meta charset="utf-8">
<title>Ringmarkt – Marktplatz</title>
<link href="https://fonts.googleapis.com/css2?family=Arimo:wght@400;700&display=swap" rel="stylesheet">
<style>
:root{
  --pink:#e2007a;
  --pink-dark:#b8005f;
  --bg:#efefef;
  --white:#ffffff;
  --text:#555555;
  --muted:#8a8a8a;
  --line:#e6e6e6;
  --tag:#cfcfcf;
}
*{box-sizing:border-box;margin:0;padding:0}
html,body{width:922px;height:1200px;overflow:hidden}
body{background:var(--bg);font-family:"Arimo",Arial,sans-serif;color:var(--text);position:relative}
.topbar{height:20px;background:var(--white);font-size:9px;color:var(--pink);display:flex;justify-content:flex-end;align-items:center;padding-right:96px;gap:5px}
.header{height:55px;background:var(--pink);position:relative}
.logo{position:absolute;left:88px;top:18px;color:var(--white);font-weight:700;font-size:16px;line-height:19px;display:flex;align-items:center;gap:5px}
.logo .dot{width:8px;height:8px;border-radius:50%;background:var(--white)}
.nav{position:absolute;left:196px;top:0;height:55px;display:flex;align-items:center;gap:26px;color:var(--white);font-size:10.5px;white-space:nowrap}
.search{position:absolute;left:651px;top:15px;width:175px;height:26px;border-radius:13px;background:var(--white)}
.search svg{position:absolute;right:10px;top:7px}
.sidebar{position:absolute;left:88px;top:99px;width:158px}
.box{background:var(--white);margin-bottom:11px;box-shadow:0 1px 2px rgba(0,0,0,.08)}
.box-head{background:var(--pink);color:var(--white);height:41px;font-size:13px;display:flex;align-items:center;padding-left:19px}
.cat-list{list-style:none;padding:0 6px 6px}
.cat-list li{height:26.5px;border-bottom:1px solid var(--line);font-size:8.3px;display:flex;align-items:center;justify-content:space-between;padding:0 9px 0 9px}
.cat-list li::after{content:"";border:3px solid transparent;border-top-color:#bbb;margin-top:3px}
.cat-list li.all{background:#eeeeee;color:var(--pink);border:none}
.cat-list li.all::after{display:none}
.promo{background:var(--pink);color:var(--white);height:146px;text-align:center;padding-top:14px;margin-bottom:11px}
.promo h3{font-size:13px;font-weight:400;margin-bottom:17px}
.promo p{font-size:8px;line-height:14.5px;padding:0 8px;white-space:nowrap}
.promo .btn{display:inline-block;margin-top:14px;width:107px;height:24px;line-height:24px;border-radius:12px;background:var(--pink-dark);color:var(--pink);font-size:8.3px;font-weight:700}
.box-body{padding:9px 6px 11px}
.box-body p{font-size:8.3px;line-height:14.7px;padding:0 9px;white-space:nowrap}
.field{height:25px;border:1px solid var(--line);border-radius:13px;font-size:8.3px;color:var(--muted);display:flex;align-items:center;padding-left:8px;margin-top:8px;position:relative}
.send{display:block;margin:4px 0 0 auto;width:77px;height:24px;border-radius:12px;background:var(--pink);color:var(--white);font-size:8.3px;font-weight:700;text-align:center;line-height:24px}
.share .field{margin-top:4px}
.share .field:first-of-type{margin-top:8px}
.share .circle{position:absolute;right:-1px;top:-1px;width:25px;height:25px;border-radius:50%;background:var(--pink)}
.foot{font-size:8.3px;color:var(--text);padding:0 6px;line-height:11px}
.foot-links{margin-top:9px;font-size:7px;line-height:9.5px}
.main{position:absolute;left:264px;top:99px;width:562px}
.main-head{height:40px;background:var(--white);display:flex;align-items:center;padding:0 19px;box-shadow:0 1px 2px rgba(0,0,0,.08)}
.main-head h1{font-size:12.5px;font-weight:400;color:var(--muted);flex:1}
.sort{font-size:8.3px;color:var(--muted);display:flex;align-items:center;gap:8px}
.sort .on{background:var(--pink);color:var(--white);border-radius:9px;padding:4px 5px}
.grid{display:flex;gap:13px;margin-top:12px}
.col{width:178px;display:flex;flex-direction:column;gap:11px}
.card{background:var(--white);box-shadow:0 1px 2px rgba(0,0,0,.1)}
.photo{position:relative}
.photo .fill{height:100%;background:linear-gradient(160deg,#d9d6d3,#f6f5f3 55%,#cfccc9)}
.photo .fill.garden{background:linear-gradient(160deg,#4e6b3a,#e9e7e2 55%,#7d8a66)}
.price{position:absolute;left:0;bottom:0;width:55px;height:28px;background:var(--pink);color:var(--white);font-size:11px;display:flex;align-items:center;justify-content:center}
.tag{position:absolute;right:0;bottom:0;width:65px;height:22px;background:var(--tag);color:var(--white);font-size:8px;display:flex;align-items:center;justify-content:center}
.info{padding:10px 12px 0}
.info h2{font-size:9.8px;font-weight:700;color:var(--pink);line-height:12.5px;letter-spacing:.2px}
.meta{display:flex;justify-content:space-between;font-size:8.2px;margin-top:5px;padding-bottom:10px}
.actions{display:flex;height:34px;border-top:1px solid var(--line)}
.actions span{flex:1;display:flex;align-items:center;justify-content:center}
.actions span+span{border-left:1px solid var(--line)}
.more{position:absolute;left:491px;top:1157px;width:107px;height:24px;border-radius:12px;background:var(--white);color:var(--pink);font-size:8.3px;font-weight:700;text-align:center;line-height:24px;box-shadow:0 1px 2px rgba(0,0,0,.12)}
</style>
</head>
<body>
<div class="topbar"><span>Hilfe</span><span>|</span><span>Anmelden</span><span>|</span><span>Warenkorb (0)</span></div>
<header class="header">
  <div class="logo"><span>Ringmarkt</span><span class="dot"></span></div>
  <nav class="nav"><span>Marktplatz</span><span>Dienstleister</span><span>Gruppen</span><span>Forum</span><span>Veranstaltungen</span><span>Über uns</span></nav>
  <div class="search"><svg width="12" height="12" viewBox="0 0 12 12"><circle cx="5" cy="5" r="3.8" fill="none" stroke="#aaa" stroke-width="1.6"/><line x1="7.8" y1="7.8" x2="11" y2="11" stroke="#aaa" stroke-width="1.8"/></svg></div>
</header>

<aside class="sidebar">
  <section class="box">
    <div class="box-head">Kategorien</div>
    <ul class="cat-list">
      <li>Brautmode</li><li>Schuhe</li><li>Accessoires</li><li>Formwäsche/ Dessous</li><li>Bräutigam</li><li>Empfang &amp; Geschenke</li><li>Dekoration</li><li class="all">Alle Kategorien</li>
    </ul>
  </section>
  <section class="promo">
    <h3>Anzeige aufgeben</h3>
    <p>Lorem ipsum dolor sit amet, con-<br>setetur sadipscing elitr, sed diam<br>nonumy eirmod tempor invidunt</p>
    <span class="btn">Neu Registrieren</span>
  </section>
  <section class="box">
    <div class="box-head">Newsletter</div>
    <div class="box-body">
      <p>Jetzt anmelden und kein Ange-<br>bot mehr verpassen</p>
      <div class="field">Emailadresse</div>
      <span class="send">Absenden</span>
    </div>
  </section>
  <section class="box share">
    <div class="box-head">Seite empfehlen</div>
    <div class="box-body">
      <p>Empfehlen und teilen Sie<br>unsere Seite mit Ihren Freund-<br>en und Bekannten</p>
      <div class="field">Empfehlen auf<span class="circle"></span></div>
      <div class="field">Teilen auf<span class="circle"></span></div>
      <div class="field">Empfehlen auf<span class="circle"></span></div>
    </div>
  </section>
  <div class="foot">
    <p>© 2014 ringmarkt.de. Alle Rechte vorbehalten.</p>
    <p class="foot-links">Über Uns &nbsp;&nbsp; Impressum &nbsp;&nbsp; Presse &nbsp;&nbsp; Jobs<br>Kontakt &nbsp;&nbsp; FAQ &nbsp;&nbsp; Datenschutzrichtlinie<br>Rechtliche Hinweise</p>
  </div>
</aside>

<main class="main">
  <div class="main-head">
    <h1>Marktplatz</h1>
    <div class="sort"><span>Sortieren nach:</span><span class="on">Datum</span><span>Preis</span></div>
  </div>
  <div class="grid">
    <div class="col">
      <article class="card"><div class="photo" style="height:216px"><div class="fill" role="img" aria-label="Kurzes weißes Brautkleid"></div><span class="price">69,00 €</span><span class="tag">Brautmode</span></div><div class="info"><h2>Traumhaftes Hochzeitskleid in weiß</h2><div class="meta"><span>22.08.2014</span><span>Köln/ Altstadt</span></div></div><div class="actions"><span><svg width="14" height="12" viewBox="0 0 14 12"><path d="M1 1h2l2 7h7l1.5-5H4" fill="none" stroke="#aaa" stroke-width="1.3"/><circle cx="6" cy="10.5" r="1" fill="#aaa"/><circle cx="11" cy="10.5" r="1" fill="#aaa"/></svg></span><span><svg width="11" height="11" viewBox="0 0 12 12"><circle cx="5" cy="5" r="3.8" fill="none" stroke="#aaa" stroke-width="1.6"/><line x1="7.8" y1="7.8" x2="11" y2="11" stroke="#aaa" stroke-width="1.8"/></svg></span></div></article>
      <article class="card"><div class="photo" style="height:270px"><div class="fill" role="img" aria-label="Langes weißes Brautkleid mit Stickerei"></div><span class="price">69,00 €</span><span class="tag">Brautmode</span></div><div class="info"><h2>Traumhaftes Hochzeitskleid in weiß</h2><div class="meta"><span>22.08.2014</span><span>Köln/ Altstadt</span></div></div><div class="actions"><span><svg width="14" height="12" viewBox="0 0 14 12"><path d="M1 1h2l2 7h7l1.5-5H4" fill="none" stroke="#aaa" stroke-width="1.3"/><circle cx="6" cy="10.5" r="1" fill="#aaa"/><circle cx="11" cy="10.5" r="1" fill="#aaa"/></svg></span><span><svg width="11" height="11" viewBox="0 0 12 12"><circle cx="5" cy="5" r="3.8" fill="none" stroke="#aaa" stroke-width="1.6"/><line x1="7.8" y1="7.8" x2="11" y2="11" stroke="#aaa" stroke-width="1.8"/></svg></span></div></article>
      <article class="card"><div class="photo" style="height:187px"><div class="fill" role="img" aria-label="Brautkleid mit gerafftem Rock, Rückansicht"></div><span class="price">69,00 €</span><span class="tag">Brautmode</span></div><div class="info"><h2>Traumhaftes Hochzeitskleid in weiß</h2><div class="meta"><span>22.08.2014</span><span>Köln/ Altstadt</span></div></div><div class="actions"><span><svg width="14" height="12" viewBox="0 0 14 12"><path d="M1 1h2l2 7h7l1.5-5H4" fill="none" stroke="#aaa" stroke-width="1.3"/><circle cx="6" cy="10.5" r="1" fill="#aaa"/><circle cx="11" cy="10.5" r="1" fill="#aaa"/></svg></span><span><svg width="11" height="11" viewBox="0 0 12 12"><circle cx="5" cy="5" r="3.8" fill="none" stroke="#aaa" stroke-width="1.6"/><line x1="7.8" y1="7.8" x2="11" y2="11" stroke="#aaa" stroke-width="1.8"/></svg></span></div></article>
    </div>
    <div class="col">
      <article class="card"><div class="photo" style="height:187px"><div class="fill" role="img" aria-label="Brautkleid mit gerafftem Rock, Rückansicht"></div><span class="price">69,00 €</span><span class="tag">Brautmode</span></div><div class="info"><h2>Traumhaftes Hochzeitskleid in weiß</h2><div class="meta"><span>22.08.2014</span><span>Köln/ Altstadt</span></div></div><div class="actions"><span><svg width="14" height="12" viewBox="0 0 14 12"><path d="M1 1h2l2 7h7l1.5-5H4" fill="none" stroke="#aaa" stroke-width="1.3"/><circle cx="6" cy="10.5" r="1" fill="#aaa"/><circle cx="11" cy="10.5" r="1" fill="#aaa"/></svg></span><span><svg width="11" height="11" viewBox="0 0 12 12"><circle cx="5" cy="5" r="3.8" fill="none" stroke="#aaa" stroke-width="1.6"/><line x1="7.8" y1="7.8" x2="11" y2="11" stroke="#aaa" stroke-width="1.8"/></svg></span></div></article>
      <article class="card"><div class="photo" style="height:215px"><div class="fill" role="img" aria-label="Kurzes Spitzenkleid in Weiß"></div><span class="price">69,00 €</span><span class="tag">Brautmode</span></div><div class="info"><h2>Traumhaftes Hochzeitskleid in weiß</h2><div class="meta"><span>22.08.2014</span><span>Köln/ Altstadt</span></div></div><div class="actions"><span><svg width="14" height="12" viewBox="0 0 14 12"><path d="M1 1h2l2 7h7l1.5-5H4" fill="none" stroke="#aaa" stroke-width="1.3"/><circle cx="6" cy="10.5" r="1" fill="#aaa"/><circle cx="11" cy="10.5" r="1" fill="#aaa"/></svg></span><span><svg width="11" height="11" viewBox="0 0 12 12"><circle cx="5" cy="5" r="3.8" fill="none" stroke="#aaa" stroke-width="1.6"/><line x1="7.8" y1="7.8" x2="11" y2="11" stroke="#aaa" stroke-width="1.8"/></svg></span></div></article>
      <article class="card"><div class="photo" style="height:271px"><div class="fill garden" role="img" aria-label="Weißes Brautkleid im Garten"></div><span class="price">69,00 €</span><span class="tag">Brautmode</span></div><div class="info"><h2>Traumhaftes Hochzeitskleid in weiß</h2><div class="meta"><span>22.08.2014</span><span>Köln/ Altstadt</span></div></div><div class="actions"><span><svg width="14" height="12" viewBox="0 0 14 12"><path d="M1 1h2l2 7h7l1.5-5H4" fill="none" stroke="#aaa" stroke-width="1.3"/><circle cx="6" cy="10.5" r="1" fill="#aaa"/><circle cx="11" cy="10.5" r="1" fill="#aaa"/></svg></span><span><svg width="11" height="11" viewBox="0 0 12 12"><circle cx="5" cy="5" r="3.8" fill="none" stroke="#aaa" stroke-width="1.6"/><line x1="7.8" y1="7.8" x2="11" y2="11" stroke="#aaa" stroke-width="1.8"/></svg></span></div></article>
    </div>
    <div class="col">
      <article class="card"><div class="photo" style="height:271px"><div class="fill garden" role="img" aria-label="Weißes Brautkleid im Garten"></div><span class="price">69,00 €</span><span class="tag">Brautmode</span></div><div class="info"><h2>Traumhaftes Hochzeitskleid in weiß</h2><div class="meta"><span>22.08.2014</span><span>Köln/ Altstadt</span></div></div><div class="actions"><span><svg width="14" height="12" viewBox="0 0 14 12"><path d="M1 1h2l2 7h7l1.5-5H4" fill="none" stroke="#aaa" stroke-width="1.3"/><circle cx="6" cy="10.5" r="1" fill="#aaa"/><circle cx="11" cy="10.5" r="1" fill="#aaa"/></svg></span><span><svg width="11" height="11" viewBox="0 0 12 12"><circle cx="5" cy="5" r="3.8" fill="none" stroke="#aaa" stroke-width="1.6"/><line x1="7.8" y1="7.8" x2="11" y2="11" stroke="#aaa" stroke-width="1.8"/></svg></span></div></article>
      <article class="card"><div class="photo" style="height:187px"><div class="fill" role="img" aria-label="Drapiertes Brautkleid mit Blütenapplikation"></div><span class="price">69,00 €</span><span class="tag">Brautmode</span></div><div class="info"><h2>Traumhaftes Hochzeitskleid in weiß</h2><div class="meta"><span>22.08.2014</span><span>Köln/ Altstadt</span></div></div><div class="actions"><span><svg width="14" height="12" viewBox="0 0 14 12"><path d="M1 1h2l2 7h7l1.5-5H4" fill="none" stroke="#aaa" stroke-width="1.3"/><circle cx="6" cy="10.5" r="1" fill="#aaa"/><circle cx="11" cy="10.5" r="1" fill="#aaa"/></svg></span><span><svg width="11" height="11" viewBox="0 0 12 12"><circle cx="5" cy="5" r="3.8" fill="none" stroke="#aaa" stroke-width="1.6"/><line x1="7.8" y1="7.8" x2="11" y2="11" stroke="#aaa" stroke-width="1.8"/></svg></span></div></article>
      <article class="card"><div class="photo" style="height:216px"><div class="fill" role="img" aria-label="Kurzes weißes Brautkleid"></div><span class="price">69,00 €</span><span class="tag">Brautmode</span></div><div class="info"><h2>Traumhaftes Hochzeitskleid in weiß</h2><div class="meta"><span>22.08.2014</span><span>Köln/ Altstadt</span></div></div><div class="actions"><span><svg width="14" height="12" viewBox="0 0 14 12"><path d="M1 1h2l2 7h7l1.5-5H4" fill="none" stroke="#aaa" stroke-width="1.3"/><circle cx="6" cy="10.5" r="1" fill="#aaa"/><circle cx="11" cy="10.5" r="1" fill="#aaa"/></svg></span><span><svg width="11" height="11" viewBox="0 0 12 12"><circle cx="5" cy="5" r="3.8" fill="none" stroke="#aaa" stroke-width="1.6"/><line x1="7.8" y1="7.8" x2="11" y2="11" stroke="#aaa" stroke-width="1.8"/></svg></span></div></article>
    </div>
  </div>
</main>
<span class="more">Mehr anziegen</span>
</body>
</html>
```